Essential Oil 15ml - package of 6

Design of a box of 6 different essential oils.
+ design of the bottle stickers
My bottles are 15ml clear blue glass.

The pictures attached are my competitors...

Target Market(s)

BRELLICK USA

Font styles to use
Serif

Requirements
Must have
• Our logo + "essential oil" and type (lavender, eucalyptus etc....)
• 15ml - 0.50 fl.oz.
• special color for the oil type.

```html
<!DOCTYPE html>
<html lang="en">
<head>
<meta charset="utf-8">
<title>Noa Vale Essential Oil Labels</title>
<link rel="stylesheet" href="https://fonts.googleapis.com/css2?family=Cinzel:wght@400;700&display=swap">
<style>
  :root {
    --paper: #ffffff;
    --gold-light: #d9a440;
    --gold-mid: #b57a1f;
    --gold-dark: #7a4c0c;
    --cream: #f2e6c8;
  }
  html, body {
    margin: 0;
    padding: 0;
    width: 1200px;
    height: 706px;
    overflow: hidden;
    background: var(--paper);
  }
  .label-row {
    position: relative;
    width: 1200px;
    height: 706px;
  }
  .label {
    position: absolute;
    top: 332px;
    width: 116px;
    height: 244px;
    font-family: "Cinzel", serif;
  }
  .label--lavender   { left: 104px; --top-a:#a634d6; --top-b:#6b1a9e; --bot-a:#4a1478; --bot-b:#1c0832; --name:#5b1890; --art:#b07ae0; }
  .label--lemon      { left: 279px; --top-a:#f6f200; --top-b:#c9be00; --bot-a:#5e5a10; --bot-b:#262408; --name:#ffe600; --art:#f2e820; }
  .label--lime       { left: 453px; --top-a:#96e600; --top-b:#4fa800; --bot-a:#2e7614; --bot-b:#133508; --name:#b2ff2a; --art:#a4f02c; }
  .label--rose       { left: 632px; --top-a:#ec1272; --top-b:#a0084a; --bot-a:#781236; --bot-b:#2e0816; --name:#ff2464; --art:#e8205a; }
  .label--eucalyptus { left: 807px; --top-a:#28e8f4; --top-b:#118ec4; --bot-a:#12627e; --bot-b:#082636; --name:#3af2ff; --art:#2ee6f2; }
  .label--apple      { left: 981px; --top-a:#38c828; --top-b:#128e12; --bot-a:#126812; --bot-b:#072e07; --name:#2fd82a; --art:#1e9a1e; }

  .stop-top-a { stop-color: var(--top-a); }
  .stop-top-b { stop-color: var(--top-b); }
  .stop-bot-a { stop-color: var(--bot-a); }
  .stop-bot-b { stop-color: var(--bot-b); }
  .stop-gold-a { stop-color: var(--gold-light); }
  .stop-gold-b { stop-color: var(--gold-dark); }

  .label-edge { fill: var(--gold-mid); }
  .label-inner-line { fill: none; stroke: var(--gold-light); stroke-width: 1.4; }
  .band-rule { stroke: var(--gold-dark); stroke-width: 1.2; }
  .tag-small { fill: var(--cream); font-size: 8.5px; }
  .tag-arc { fill: var(--cream); font-size: 9.5px; letter-spacing: 1px; }
  .brand-mark { fill: var(--gold-mid); opacity: .9; }
  .brand-name { fill: var(--gold-mid); font-size: 17px; font-weight: 700; }
  .oil-name { fill: var(--name); font-size: 13px; font-weight: 700; letter-spacing: .5px; }
  .grade { fill: var(--cream); font-size: 11.5px; }
  .volume { fill: var(--cream); font-size: 8px; }
  .oil-art { fill: var(--art); opacity: .75; }
</style>
</head>
<body>
<main class="label-row">

  <!-- Lavender -->
  <svg class="label label--lavender" viewBox="0 0 145 305" role="group" aria-label="Lavender essential oil label">
    <defs>
      <linearGradient id="lav-top" x1="0" y1="0" x2="0" y2="1"><stop offset="0" class="stop-top-a"/><stop offset="1" class="stop-top-b"/></linearGradient>
      <linearGradient id="lav-bot" x1="0" y1="0" x2="0" y2="1"><stop offset="0" class="stop-bot-a"/><stop offset="1" class="stop-bot-b"/></linearGradient>
      <linearGradient id="lav-band" x1="0" y1="0" x2="1" y2="0"><stop offset="0" class="stop-gold-b"/><stop offset=".5" class="stop-gold-a"/><stop offset="1" class="stop-gold-b"/></linearGradient>
      <clipPath id="lav-clip"><path d="M5,34 H32 Q72.5,-4 113,34 H140 V271 H113 Q72.5,309 32,271 H5 Z"/></clipPath>
      <path id="lav-arc" d="M40,38 Q72.5,12 105,38"/>
    </defs>
    <path class="label-edge" d="M0,30 H30 Q72.5,-12 115,30 H145 V275 H115 Q72.5,317 30,275 H0 Z"/>
    <g clip-path="url(#lav-clip)">
      <rect x="0" y="0" width="145" height="140" fill="url(#lav-top)"/>
      <rect x="0" y="140" width="145" height="30" fill="url(#lav-band)"/>
      <rect x="0" y="170" width="145" height="135" fill="url(#lav-bot)"/>
      <rect class="oil-art" x="40" y="180" width="45" height="120" rx="18" role="img" aria-label="Lavender sprig illustration"/>
    </g>
    <line class="band-rule" x1="5" y1="140" x2="140" y2="140"/>
    <line class="band-rule" x1="5" y1="170" x2="140" y2="170"/>
    <path class="label-inner-line" d="M5,34 H32 Q72.5,-4 113,34 H140 V271 H113 Q72.5,309 32,271 H5 Z"/>
    <text class="tag-arc"><textPath href="#lav-arc" startOffset="50%" text-anchor="middle">ESSENTIAL</textPath></text>
    <text class="tag-small" x="9" y="43">100%</text>
    <text class="tag-small" x="136" y="43" text-anchor="end">OIL</text>
    <circle class="brand-mark" cx="72.5" cy="66" r="15"/>
    <text class="brand-name" x="72.5" y="121" text-anchor="middle">NOA VALE</text>
    <text class="oil-name" x="72.5" y="161" text-anchor="middle">LAVENDER</text>
    <text class="grade" x="72.5" y="200" text-anchor="middle">PURE</text>
    <text class="grade" x="72.5" y="226" text-anchor="middle">THERAPEUTIC</text>
    <text class="grade" x="72.5" y="252" text-anchor="middle">GRADE</text>
    <text class="volume" x="72.5" y="295" text-anchor="middle">15 ML</text>
  </svg>

  <!-- Lemon -->
  <svg class="label label--lemon" viewBox="0 0 145 305" role="group" aria-label="Lemon essential oil label">
    <defs>
      <linearGradient id="lem-top" x1="0" y1="0" x2="0" y2="1"><stop offset="0" class="stop-top-a"/><stop offset="1" class="stop-top-b"/></linearGradient>
      <linearGradient id="lem-bot" x1="0" y1="0" x2="0" y2="1"><stop offset="0" class="stop-bot-a"/><stop offset="1" class="stop-bot-b"/></linearGradient>
      <linearGradient id="lem-band" x1="0" y1="0" x2="1" y2="0"><stop offset="0" class="stop-gold-b"/><stop offset=".5" class="stop-gold-a"/><stop offset="1" class="stop-gold-b"/></linearGradient>
      <clipPath id="lem-clip"><path d="M5,34 H32 Q72.5,-4 113,34 H140 V271 H113 Q72.5,309 32,271 H5 Z"/></clipPath>
      <path id="lem-arc" d="M40,38 Q72.5,12 105,38"/>
    </defs>
    <path class="label-edge" d="M0,30 H30 Q72.5,-12 115,30 H145 V275 H115 Q72.5,317 30,275 H0 Z"/>
    <g clip-path="url(#lem-clip)">
      <rect x="0" y="0" width="145" height="140" fill="url(#lem-top)"/>
      <rect x="0" y="140" width="145" height="30" fill="url(#lem-band)"/>
      <rect x="0" y="170" width="145" height="135" fill="url(#lem-bot)"/>
      <rect class="oil-art" x="28" y="236" width="82" height="50" rx="24" role="img" aria-label="Lemon fruit illustration"/>
    </g>
    <line class="band-rule" x1="5" y1="140" x2="140" y2="140"/>
    <line class="band-rule" x1="5" y1="170" x2="140" y2="170"/>
    <path class="label-inner-line" d="M5,34 H32 Q72.5,-4 113,34 H140 V271 H113 Q72.5,309 32,271 H5 Z"/>
    <text class="tag-arc"><textPath href="#lem-arc" startOffset="50%" text-anchor="middle">ESSENTIAL</textPath></text>
    <text class="tag-small" x="9" y="43">100%</text>
    <text class="tag-small" x="136" y="43" text-anchor="end">OIL</text>
    <circle class="brand-mark" cx="72.5" cy="66" r="15"/>
    <text class="brand-name" x="72.5" y="121" text-anchor="middle">NOA VALE</text>
    <text class="oil-name" x="72.5" y="161" text-anchor="middle">LEMON</text>
    <text class="grade" x="72.5" y="200" text-anchor="middle">PURE</text>
    <text class="grade" x="72.5" y="226" text-anchor="middle">THERAPEUTIC</text>
    <text class="grade" x="72.5" y="252" text-anchor="middle">GRADE</text>
    <text class="volume" x="72.5" y="295" text-anchor="middle">15 ML</text>
  </svg>

  <!-- Lime -->
  <svg class="label label--lime" viewBox="0 0 145 305" role="group" aria-label="Lime essential oil label">
    <defs>
      <linearGradient id="lim-top" x1="0" y1="0" x2="0" y2="1"><stop offset="0" class="stop-top-a"/><stop offset="1" class="stop-top-b"/></linearGradient>
      <linearGradient id="lim-bot" x1="0" y1="0" x2="0" y2="1"><stop offset="0" class="stop-bot-a"/><stop offset="1" class="stop-bot-b"/></linearGradient>
      <linearGradient id="lim-band" x1="0" y1="0" x2="1" y2="0"><stop offset="0" class="stop-gold-b"/><stop offset=".5" class="stop-gold-a"/><stop offset="1" class="stop-gold-b"/></linearGradient>
      <clipPath id="lim-clip"><path d="M5,34 H32 Q72.5,-4 113,34 H140 V271 H113 Q72.5,309 32,271 H5 Z"/></clipPath>
      <path id="lim-arc" d="M40,38 Q72.5,12 105,38"/>
    </defs>
    <path class="label-edge" d="M0,30 H30 Q72.5,-12 115,30 H145 V275 H115 Q72.5,317 30,275 H0 Z"/>
    <g clip-path="url(#lim-clip)">
      <rect x="0" y="0" width="145" height="140" fill="url(#lim-top)"/>
      <rect x="0" y="140" width="145" height="30" fill="url(#lim-band)"/>
      <rect x="0" y="170" width="145" height="135" fill="url(#lim-bot)"/>
      <rect class="oil-art" x="36" y="220" width="86" height="62" rx="28" role="img" aria-label="Lime fruit illustration"/>
    </g>
    <line class="band-rule" x1="5" y1="140" x2="140" y2="140"/>
    <line class="band-rule" x1="5" y1="170" x2="140" y2="170"/>
    <path class="label-inner-line" d="M5,34 H32 Q72.5,-4 113,34 H140 V271 H113 Q72.5,309 32,271 H5 Z"/>
    <text class="tag-arc"><textPath href="#lim-arc" startOffset="50%" text-anchor="middle">ESSENTIAL</textPath></text>
    <text class="tag-small" x="9" y="43">100%</text>
    <text class="tag-small" x="136" y="43" text-anchor="end">OIL</text>
    <circle class="brand-mark" cx="72.5" cy="66" r="15"/>
    <text class="brand-name" x="72.5" y="121" text-anchor="middle">NOA VALE</text>
    <text class="oil-name" x="72.5" y="161" text-anchor="middle">LIME</text>
    <text class="grade" x="72.5" y="200" text-anchor="middle">PURE</text>
    <text class="grade" x="72.5" y="226" text-anchor="middle">THERAPEUTIC</text>
    <text class="grade" x="72.5" y="252" text-anchor="middle">GRADE</text>
    <text class="volume" x="72.5" y="295" text-anchor="middle">15 ML</text>
  </svg>

  <!-- Rose -->
  <svg class="label label--rose" viewBox="0 0 145 305" role="group" aria-label="Rose essential oil label">
    <defs>
      <linearGradient id="ros-top" x1="0" y1="0" x2="0" y2="1"><stop offset="0" class="stop-top-a"/><stop offset="1" class="stop-top-b"/></linearGradient>
      <linearGradient id="ros-bot" x1="0" y1="0" x2="0" y2="1"><stop offset="0" class="stop-bot-a"/><stop offset="1" class="stop-bot-b"/></linearGradient>
      <linearGradient id="ros-band" x1="0" y1="0" x2="1" y2="0"><stop offset="0" class="stop-gold-b"/><stop offset=".5" class="stop-gold-a"/><stop offset="1" class="stop-gold-b"/></linearGradient>
      <clipPath id="ros-clip"><path d="M5,34 H32 Q72.5,-4 113,34 H140 V271 H113 Q72.5,309 32,271 H5 Z"/></clipPath>
      <path id="ros-arc" d="M40,38 Q72.5,12 105,38"/>
    </defs>
    <path class="label-edge" d="M0,30 H30 Q72.5,-12 115,30 H145 V275 H115 Q72.5,317 30,275 H0 Z"/>
    <g clip-path="url(#ros-clip)">
      <rect x="0" y="0" width="145" height="140" fill="url(#ros-top)"/>
      <rect x="0" y="140" width="145" height="30" fill="url(#ros-band)"/>
      <rect x="0" y="170" width="145" height="135" fill="url(#ros-bot)"/>
      <rect class="oil-art" x="38" y="240" width="70" height="56" rx="26" role="img" aria-label="Rose flower illustration"/>
    </g>
    <line class="band-rule" x1="5" y1="140" x2="140" y2="140"/>
    <line class="band-rule" x1="5" y1="170" x2="140" y2="170"/>
    <path class="label-inner-line" d="M5,34 H32 Q72.5,-4 113,34 H140 V271 H113 Q72.5,309 32,271 H5 Z"/>
    <text class="tag-arc"><textPath href="#ros-arc" startOffset="50%" text-anchor="middle">ESSENTIAL</textPath></text>
    <text class="tag-small" x="9" y="43">100%</text>
    <text class="tag-small" x="136" y="43" text-anchor="end">OIL</text>
    <circle class="brand-mark" cx="72.5" cy="66" r="15"/>
    <text class="brand-name" x="72.5" y="121" text-anchor="middle">NOA VALE</text>
    <text class="oil-name" x="72.5" y="161" text-anchor="middle">ROSE</text>
    <text class="grade" x="72.5" y="200" text-anchor="middle">PURE</text>
    <text class="grade" x="72.5" y="226" text-anchor="middle">THERAPEUTIC</text>
    <text class="grade" x="72.5" y="252" text-anchor="middle">GRADE</text>
    <text class="volume" x="72.5" y="295" text-anchor="middle">15 ML</text>
  </svg>

  <!-- Eucalyptus -->
  <svg class="label label--eucalyptus" viewBox="0 0 145 305" role="group" aria-label="Eucalyptus essential oil label">
    <defs>
      <linearGradient id="euc-top" x1="0" y1="0" x2="0" y2="1"><stop offset="0" class="stop-top-a"/><stop offset="1" class="stop-top-b"/></linearGradient>
      <linearGradient id="euc-bot" x1="0" y1="0" x2="0" y2="1"><stop offset="0" class="stop-bot-a"/><stop offset="1" class="stop-bot-b"/></linearGradient>
      <linearGradient id="euc-band" x1="0" y1="0" x2="1" y2="0"><stop offset="0" class="stop-gold-b"/><stop offset=".5" class="stop-gold-a"/><stop offset="1" class="stop-gold-b"/></linearGradient>
      <clipPath id="euc-clip"><path d="M5,34 H32 Q72.5,-4 113,34 H140 V271 H113 Q72.5,309 32,271 H5 Z"/></clipPath>
      <path id="euc-arc" d="M40,38 Q72.5,12 105,38"/>
    </defs>
    <path class="label-edge" d="M0,30 H30 Q72.5,-12 115,30 H145 V275 H115 Q72.5,317 30,275 H0 Z"/>
    <g clip-path="url(#euc-clip)">
      <rect x="0" y="0" width="145" height="140" fill="url(#euc-top)"/>
      <rect x="0" y="140" width="145" height="30" fill="url(#euc-band)"/>
      <rect x="0" y="170" width="145" height="135" fill="url(#euc-bot)"/>
      <rect class="oil-art" x="14" y="220" width="110" height="66" rx="30" role="img" aria-label="Eucalyptus leaves illustration"/>
    </g>
    <line class="band-rule" x1="5" y1="140" x2="140" y2="140"/>
    <line class="band-rule" x1="5" y1="170" x2="140" y2="170"/>
    <path class="label-inner-line" d="M5,34 H32 Q72.5,-4 113,34 H140 V271 H113 Q72.5,309 32,271 H5 Z"/>
    <text class="tag-arc"><textPath href="#euc-arc" startOffset="50%" text-anchor="middle">ESSENTIAL</textPath></text>
    <text class="tag-small" x="9" y="43">100%</text>
    <text class="tag-small" x="136" y="43" text-anchor="end">OIL</text>
    <circle class="brand-mark" cx="72.5" cy="66" r="15"/>
    <text class="brand-name" x="72.5" y="121" text-anchor="middle">NOA VALE</text>
    <text class="oil-name" x="72.5" y="161" text-anchor="middle" textLength="122" lengthAdjust="spacingAndGlyphs">EUCALIPTUS</text>
    <text class="grade" x="72.5" y="200" text-anchor="middle">PURE</text>
    <text class="grade" x="72.5" y="226" text-anchor="middle">THERAPEUTIC</text>
    <text class="grade" x="72.5" y="252" text-anchor="middle">GRADE</text>
    <text class="volume" x="72.5" y="295" text-anchor="middle">15 ML</text>
  </svg>

  <!-- Apple -->
  <svg class="label label--apple" viewBox="0 0 145 305" role="group" aria-label="Apple essential oil label">
    <defs>
      <linearGradient id="app-top" x1="0" y1="0" x2="0" y2="1"><stop offset="0" class="stop-top-a"/><stop offset="1" class="stop-top-b"/></linearGradient>
      <linearGradient id="app-bot" x1="0" y1="0" x2="0" y2="1"><stop offset="0" class="stop-bot-a"/><stop offset="1" class="stop-bot-b"/></linearGradient>
      <linearGradient id="app-band" x1="0" y1="0" x2="1" y2="0"><stop offset="0" class="stop-gold-b"/><stop offset=".5" class="stop-gold-a"/><stop offset="1" class="stop-gold-b"/></linearGradient>
      <clipPath id="app-clip"><path d="M5,34 H32 Q72.5,-4 113,34 H140 V271 H113 Q72.5,309 32,271 H5 Z"/></clipPath>
      <path id="app-arc" d="M40,38 Q72.5,12 105,38"/>
    </defs>
    <path class="label-edge" d="M0,30 H30 Q72.5,-12 115,30 H145 V275 H115 Q72.5,317 30,275 H0 Z"/>
    <g clip-path="url(#app-clip)">
      <rect x="0" y="0" width="145" height="140" fill="url(#app-top)"/>
      <rect x="0" y="140" width="145" height="30" fill="url(#app-band)"/>
      <rect x="0" y="170" width="145" height="135" fill="url(#app-bot)"/>
      <rect class="oil-art" x="44" y="218" width="66" height="66" rx="33" role="img" aria-label="Apple fruit illustration"/>
    </g>
    <line class="band-rule" x1="5" y1="140" x2="140" y2="140"/>
    <line class="band-rule" x1="5" y1="170" x2="140" y2="170"/>
    <path class="label-inner-line" d="M5,34 H32 Q72.5,-4 113,34 H140 V271 H113 Q72.5,309 32,271 H5 Z"/>
    <text class="tag-arc"><textPath href="#app-arc" startOffset="50%" text-anchor="middle">ESSENTIAL</textPath></text>
    <text class="tag-small" x="9" y="43">100%</text>
    <text class="tag-small" x="136" y="43" text-anchor="end">OIL</text>
    <circle class="brand-mark" cx="72.5" cy="66" r="15"/>
    <text class="brand-name" x="72.5" y="121" text-anchor="middle">NOA VALE</text>
    <text class="oil-name" x="72.5" y="161" text-anchor="middle">APPLE</text>
    <text class="grade" x="72.5" y="200" text-anchor="middle">PURE</text>
    <text class="grade" x="72.5" y="226" text-anchor="middle">THERAPEUTIC</text>
    <text class="grade" x="72.5" y="252" text-anchor="middle">GRADE</text>
    <text class="volume" x="72.5" y="295" text-anchor="middle">15 ML</text>
  </svg>

</main>
</body>
</html>
```